Business card design for Healthcare Clinic

Need to create an elegant business card design that incorporates a QR code to a specific page on the website

Industry/Entity Type

Healthcare

Contact Information for Business Card

Name, job title, address, phone number, fax number, website

Font styles to use
Serif
Sans Serif

Colors
0054AA
0677BA
7BADD7
CADEEF
E8F1F8
0094D4
00A9DD
6FCCEA
C7EBF8
E9F6FB
6B429C
8869AF
B7A5CE
E3DAEB
F3F0F8

Requirements
Must have
• QR Code on the back side that will link to a specific website page (use place holder for now)
Nice to have
• Maybe try to incorporate the logo design elements (DNA strand) into the design. Please inquire for website if you want to see.

```html
<!DOCTYPE html>
<html lang="en">
<head>
<meta charset="utf-8">
<title>Northbrook Motion Health Clinic – Business Card</title>
<link href="https://fonts.googleapis.com/css2?family=Playfair+Display:wght@700&family=Poppins:wght@400;500&display=swap" rel="stylesheet">
<style>
  :root {
    --stage: #3b3b3d;
    --navy: #38358a;
    --sky: #4aa8dc;
    --ink: #1d1d2b;
    --white: #ffffff;
    --serif: "Playfair Display", Georgia, serif;
    --sans: "Poppins", Arial, sans-serif;
  }
  * { box-sizing: border-box; margin: 0; padding: 0; }
  html, body { width: 1200px; height: 689px; overflow: hidden; }
  body {
    background: var(--stage);
    display: flex;
    align-items: center;
    justify-content: center;
    gap: 40px;
    font-family: var(--sans);
  }
  .card {
    position: relative;
    width: 540px;
    height: 310px;
    border-radius: 22px;
    overflow: hidden;
  }
  /* Back side */
  .card--back { background: var(--navy); }
  .helix-art {
    position: absolute;
    left: 36px; top: 20px;
    width: 150px; height: 270px;
    border-radius: 70px;
    background: linear-gradient(160deg, #5a58b0 0%, #6fb7e4 50%, #4b48a0 100%);
    opacity: .55;
  }
  .back-brand {
    position: absolute;
    left: 210px; top: 96px;
    width: 300px;
  }
  .brand-name {
    font-family: var(--serif);
    font-weight: 700;
    line-height: 1.15;
  }
  .back-brand .brand-name { color: var(--white); font-size: 27px; }
  .brand-tag {
    margin-top: 6px;
    font-size: 10px;
    letter-spacing: 5px;
    color: var(--sky);
  }
  .qr-placeholder {
    position: absolute;
    right: 30px; bottom: 26px;
    width: 72px; height: 72px;
    border-radius: 6px;
    background: var(--white);
    border: 6px solid var(--white);
    outline: 2px solid var(--sky);
  }
  /* Front side */
  .card--front { background: var(--white); }
  .front-brand {
    position: absolute;
    left: 36px; top: 34px;
    width: 340px;
  }
  .front-brand .brand-name { color: var(--navy); font-size: 26px; }
  .person {
    position: absolute;
    left: 36px; top: 150px;
  }
  .person-name {
    font-family: var(--serif);
    font-weight: 700;
    font-size: 24px;
    color: var(--navy);
  }
  .person-title {
    font-size: 15px;
    color: var(--sky);
  }
  .divider {
    position: absolute;
    left: 262px; top: 140px;
    width: 1px; height: 72px;
    background: var(--navy);
  }
  .contacts {
    position: absolute;
    left: 278px; top: 138px;
    list-style: none;
    font-size: 14px;
    color: var(--ink);
    line-height: 25px;
  }
  .contacts li { display: flex; align-items: center; gap: 8px; white-space: nowrap; }
  .contacts svg { width: 14px; height: 14px; fill: var(--navy); flex: none; }
  .contacts .domain { color: var(--navy); }
  .address-band {
    position: absolute;
    left: 0; right: 0; bottom: 0;
    height: 62px;
    background: var(--navy);
    border-top: 5px solid var(--sky);
    display: flex;
    align-items: center;
    padding-left: 36px;
    color: var(--white);
    font-size: 15px;
  }
</style>
</head>
<body>
  <section class="card card--back">
    <div class="helix-art" role="img" aria-label="Decorative DNA helix illustration in blue tones"></div>
    <div class="back-brand">
      <p class="brand-name">Northbrook Motion Health Clinic</p>
      <p class="brand-tag">Care &amp; Recovery</p>
    </div>
    <div class="qr-placeholder" role="img" aria-label="QR code placeholder linking to a clinic web page"></div>
  </section>

  <section class="card card--front">
    <div class="front-brand">
      <p class="brand-name">Northbrook Motion Health Clinic</p>
      <p class="brand-tag">Care &amp; Recovery</p>
    </div>
    <div class="person">
      <p class="person-name">Daniel Reyes</p>
      <p class="person-title">Managing Director</p>
    </div>
    <div class="divider"></div>
    <ul class="contacts">
      <li>
        <svg viewBox="0 0 24 24" aria-hidden="true"><path d="M6.6 10.8a15 15 0 0 0 6.6 6.6l2.2-2.2a1 1 0 0 1 1-.25 11.4 11.4 0 0 0 3.6.57 1 1 0 0 1 1 1V20a1 1 0 0 1-1 1A17 17 0 0 1 3 4a1 1 0 0 1 1-1h3.5a1 1 0 0 1 1 1c0 1.250.2 2.450.57 3.57a1 1 0 0 1-.25 1z"/></svg>
        <span>055-210 384 617</span>
      </li>
      <li>
        <svg viewBox="0 0 24 24" aria-hidden="true"><path d="M6 2h9l3 3v5H6zM4 11h16a2 2 0 0 1 2 2v6h-4v3H6v-3H2v-6a2 2 0 0 1 2-2zm4 6v3h8v-3z"/></svg>
        <span>055-210 384 618</span>
      </li>
      <li>
        <svg viewBox="0 0 24 24" aria-hidden="true"><path d="M12 2a10 10 0 1 0 0 20 10 10 0 0 0 0-20zm6.9 9h-3a15 15 0 0 0-1.3-5.6A8 8 0 0 1 18.900 11zM12 4c.9 1.200 1.800 3.600 1.900 7h-3.8c.1-3.4 1-5.8 1.9-7zM9.4 5.4A15 15 0 0 0 8.1 11h-3a8 8 0 0 1 4.3-5.6zM5.1 13h3a15 15 0 0 0 1.3 5.6A8 8 0 0 1 5.1 13zM12 20c-.9-1.2-1.8-3.6-1.9-7h3.8c-.1 3.4-1 5.8-1.9 7zm2.6-1.4a15 15 0 0 0 1.3-5.6h3a8 8 0 0 1-4.3 5.6z"/></svg>
        <span>www.<span class="domain">northbrookclinic</span>.com</span>
      </li>
    </ul>
    <div class="address-band">88 Linden Avenue, Suite 4, Riverton 20418</div>
  </section>
</body>
</html>
```